Breezeway Climate Business Card Design

Design new, 2 sides, business cards for a residential and light commercial heating, air conditioning contractor.

Target Market(s)

Homeowners, small businesses

Industry/Entity Type

Business

Contact Information for Business Card

Dominic Vasquerelli
Phone - 555-214-6837
Email
Address - PO box 618
Millbrook NJ 07999
Website - www.BreezewayClimateLLC.example

Requirements
Must have
• logo, company colors, standard size with no die cut, so I can use printhaven

```html
<!DOCTYPE html>
<html lang="en">
<head>
<meta charset="utf-8">
<title>Breezeway Climate Business Card</title>
<link rel="stylesheet" href="https://fonts.googleapis.com/css2?family=Open+Sans:wght@400;600;700&display=swap">
<style>
  :root {
    --backdrop: #e9e6e2;
    --card-front: #ffffff;
    --card-back: #1c1c1c;
    --ink: #1a1a1a;
    --brand-light: #8a8a8a;
    --shadow: rgba(0,0,0,0.25);
  }
  * { margin: 0; padding: 0; box-sizing: border-box; }
  html, body {
    width: 1200px; height: 1000px; overflow: hidden;
    background: var(--backdrop);
    font-family: "Open Sans", sans-serif;
    color: var(--ink);
  }
  .canvas { position: relative; width: 1200px; height: 1000px; }
  .card {
    position: absolute; left: 266px; width: 666px; height: 397px;
    border-radius: 22px;
    box-shadow: 0 4px 14px var(--shadow);
  }
  .card-front { top: 74px; background: var(--card-front); }
  .card-back { top: 534px; background: var(--card-back); display: flex; align-items: center; justify-content: center; }

  .brand-lockup {
    position: absolute; left: 300px; top: 198px; width: 290px;
    display: flex; align-items: center; gap: 12px;
  }
  .brand-mark { width: 26px; height: 26px; border-radius: 50%; background: var(--ink); flex: none; }
  .brand-name { font-size: 30px; font-weight: 700; line-height: 1.12; color: var(--ink); }

  .card-back .brand-lockup { position: static; width: auto; }
  .card-back .brand-mark { background: var(--brand-light); width: 34px; height: 34px; }
  .card-back .brand-name { color: var(--brand-light); font-size: 40px; }

  .contact-block { position: absolute; left: 358px; top: 102px; }
  .person-name { font-size: 17px; font-weight: 700; line-height: 24px; }
  .person-title { font-size: 16px; line-height: 22px; }
  .company-name { margin-top: 14px; font-size: 15px; font-weight: 700; line-height: 22px; }
  .company-address { font-size: 16px; line-height: 24px; }
  .contact-list { list-style: none; margin-top: 16px; }
  .contact-list li { display: flex; align-items: center; gap: 8px; font-size: 16px; line-height: 22.5px; }
  .contact-list svg { width: 16px; height: 14px; flex: none; fill: var(--ink); }
</style>
</head>
<body>
<main class="canvas">
  <section class="card card-front" aria-label="Card front">
    <div class="brand-lockup" style="left:34px;top:122px;">
      <span class="brand-mark"></span>
      <span class="brand-name">Breezeway Climate</span>
    </div>
    <div class="contact-block">
      <p class="person-name">Dominic Vasquerelli</p>
      <p class="person-title">Vice President</p>
      <p class="company-name">Breezeway Climate LLC</p>
      <p class="company-address">PO box 618 Millbrook NJ 07999</p>
      <ul class="contact-list">
        <li>
          <svg viewBox="0 0 16 14" aria-hidden="true"><path d="M1 5c0-2 2-3 7-3s7 1 7 3v1h-3V4.5H4V6H1z"/><rect x="3" y="7" width="10" height="6" rx="1"/></svg>
          555-214-6837
        </li>
        <li>
          <svg viewBox="0 0 16 14" aria-hidden="true"><path d="M1 2h14v10H1z M2 3l6 5 6-5" fill="none" stroke="#1a1a1a" stroke-width="1.6"/><path d="M1 2h14L8 8z"/></svg>
          info@breezewayclimatellc.example
        </li>
        <li>
          <svg viewBox="0 0 16 14" aria-hidden="true"><circle cx="7" cy="7" r="6" fill="none" stroke="#1a1a1a" stroke-width="1.6"/><path d="M1 7h12M7 1c-3 3-3 9 0 12M7 1c3 3 3 9 0 12" fill="none" stroke="#1a1a1a" stroke-width="1.2"/></svg>
          www.BreezewayClimateLLC.example
        </li>
      </ul>
    </div>
  </section>

  <section class="card card-back" aria-label="Card back">
    <div class="brand-lockup">
      <span class="brand-mark"></span>
      <span class="brand-name">Breezeway Climate</span>
    </div>
  </section>
</main>
</body>
</html>
```